Tasman Curdworks Guild needs new business cards

We need new business cards designed and produced. We are likely to need other design work done for ads, flyers etc in future.

We would like to start with an initial business card.

The Tasman Curdworks Guild (TCG) is a membership-based not-for-profit organisation that looks after the interests of Australia's small to medium artisan cheesemakers, many of whom are also small-scale farmers. The design should be simple, using our logo, but also communicate our artisan cheese and small dairy farm focus.

The first card to be designed and produced is for me, Miriam Tolhurst. My details are:

Miriam Tolhurst
Secretary
Tasman Curdworks Guild (TCG)
http://www.curdworksguild.example
T +61452837190
E miriam.miriamtolhurst@mailbox.example

I have attached the TCG logo in jpg form. I have a higher resolution version available if needed.

Thank you!

Miriam

Miriam Tolhurst
Tasman Curdworks Guild
miriam.miriamtolhurst@mailbox.example
+61452837190

Sans Serif

• Logo (see attached file)

```html
<!DOCTYPE html>
<html lang="en">
<head>
<meta charset="utf-8">
<title>Tasman Curdworks Guild – Business Card</title>
<link rel="stylesheet" href="https://fonts.googleapis.com/css2?family=Montserrat:wght@400;600&display=swap">
<style>
  :root {
    --backdrop: #3a3a3a;
    --cheese: #fdc965;
    --paper: #ffffff;
    --rind: #4a1e0a;
    --muted: #6b6b6b;
  }
  html, body {
    margin: 0;
    width: 1200px;
    height: 855px;
    overflow: hidden;
    background: var(--backdrop);
    font-family: "Montserrat", sans-serif;
  }
  .sheet {
    width: 1200px;
    height: 855px;
    display: flex;
    align-items: center;
    justify-content: center;
    gap: 40px;
  }
  .card {
    position: relative;
    width: 530px;
    height: 303px;
    box-sizing: border-box;
    box-shadow: 0 10px 30px rgba(0,0,0,0.45);
  }
  .card--front {
    background: var(--cheese);
    display: flex;
    align-items: center;
    justify-content: center;
  }
  .card--back {
    background: var(--paper);
    padding: 36px 40px;
  }
  .brand {
    display: flex;
    align-items: center;
    gap: 14px;
  }
  .brand__dot {
    flex: none;
    border-radius: 50%;
  }
  .brand__name {
    font-weight: 400;
    line-height: 1.1;
  }
  .card--front .brand__dot {
    width: 46px;
    height: 46px;
    background: var(--paper);
  }
  .card--front .brand__name {
    color: var(--paper);
    font-size: 26px;
  }
  .card--back .brand__dot {
    width: 34px;
    height: 34px;
    background: var(--cheese);
  }
  .card--back .brand__name {
    color: var(--rind);
    font-size: 19px;
  }
  .person {
    position: absolute;
    left: 44px;
    bottom: 92px;
  }
  .person__name {
    margin: 0;
    font-size: 22px;
    font-weight: 600;
    color: var(--rind);
  }
  .person__role {
    margin: 2px 0 0;
    font-size: 14px;
    color: var(--muted);
    letter-spacing: 0.03em;
  }
  .contact {
    position: absolute;
    left: 44px;
    bottom: 30px;
    margin: 0;
    padding: 0;
    list-style: none;
    font-size: 13.5px;
    color: var(--muted);
  }
  .contact__item {
    display: flex;
    align-items: center;
    gap: 9px;
    line-height: 1.55;
  }
  .contact__icon {
    width: 13px;
    height: 13px;
    flex: none;
  }
</style>
</head>
<body>
  <main class="sheet">
    <section class="card card--front" aria-label="Card front">
      <div class="brand">
        <span class="brand__dot"></span>
        <span class="brand__name">Tasman<br>Curdworks<br>Guild</span>
      </div>
    </section>

    <section class="card card--back" aria-label="Card back">
      <div class="brand">
        <span class="brand__dot"></span>
        <span class="brand__name">Tasman<br>Curdworks<br>Guild</span>
      </div>

      <div class="person">
        <p class="person__name">Miriam Tolhurst</p>
        <p class="person__role">Secretary</p>
      </div>

      <ul class="contact">
        <li class="contact__item">
          <svg class="contact__icon" viewBox="0 0 16 16" aria-hidden="true">
            <path d="M4 1 L6.5 4.5 L5 6.2 C6 8.4 7.6 10 9.8 11 L11.5 9.5 L15 12 L13.2 14.6 C7 14 2 9 1.4 2.8 Z" fill="var(--rind)"/>
          </svg>
          +61452837190
        </li>
        <li class="contact__item">
          <svg class="contact__icon" viewBox="0 0 16 16" aria-hidden="true">
            <rect x="1" y="3.5" width="14" height="9.5" fill="var(--rind)"/>
            <path d="M1.5 4 L8 9 L14.5 4" fill="none" stroke="#fff" stroke-width="1.2"/>
          </svg>
          miriam.miriamtolhurst@mailbox.example
        </li>
      </ul>
    </section>
  </main>
</body>
</html>
```